Full re-design of visual identity

We have just re-designed our logo and would like to apply it on our folders, business cards, stationery, and etc... we are attaching new logo + the material we need to re-design... we will provide full corel draw files to help make job easier and also because lot of icons and artwork can be still used...

any doubts we are at your disposal. thanks in advance.

Business

```html
<!DOCTYPE html>
<html lang="en">
<head>
<meta charset="UTF-8">
<title>Lumora Business Cards</title>
<link rel="stylesheet" href="https://fonts.googleapis.com/css2?family=Exo+2:wght@300;400;600&display=swap">
<style>
  :root {
    --canvas: #f3f3f3;
    --card: #ffffff;
    --orange: #ec7f3f;
    --orange-soft: #f08a4b;
    --grey-text: #6e6e70;
    --grey-name: #6a6a6c;
    --white: #ffffff;
    --shadow: rgba(0, 0, 0, 0.12);
  }
  * { box-sizing: border-box; margin: 0; padding: 0; }
  html, body {
    width: 1200px;
    height: 1000px;
    overflow: hidden;
    background: var(--canvas);
    font-family: "Exo 2", sans-serif;
  }
  .canvas {
    width: 1200px;
    height: 1000px;
    display: flex;
    flex-direction: column;
    align-items: center;
    justify-content: center;
    gap: 70px;
  }
  .card {
    width: 600px;
    height: 343px;
    background: var(--card);
    box-shadow: 0 12px 30px var(--shadow);
    position: relative;
    overflow: hidden;
  }

  /* Back card */
  .card--back { display: flex; }
  .card__info {
    width: 46%;
    padding: 60px 0 0 40px;
  }
  .card__panel {
    flex: 1;
    background: linear-gradient(135deg, var(--orange-soft), var(--orange));
    color: var(--white);
    display: flex;
    flex-direction: column;
    justify-content: center;
    padding-left: 44px;
  }
  .person__name {
    font-weight: 300;
    font-size: 38px;
    letter-spacing: 0.5px;
  }
  .person__role {
    font-weight: 300;
    font-size: 14px;
    margin-top: 4px;
    padding-left: 2px;
  }

  .brand__name {
    font-weight: 600;
    color: var(--grey-name);
    line-height: 1;
    letter-spacing: 0.5px;
  }
  .brand__tagline {
    color: var(--grey-text);
    font-weight: 400;
  }
  .card__info .brand__name { font-size: 30px; }
  .card__info .brand__tagline { font-size: 9px; margin-top: 5px; }

  .contacts {
    list-style: none;
    margin-top: 26px;
    margin-left: 44px;
    color: var(--grey-text);
    font-size: 11.5px;
    font-weight: 400;
  }
  .contacts__item {
    display: flex;
    gap: 10px;
    align-items: flex-start;
    margin-bottom: 6px;
    line-height: 1.35;
  }
  .contacts__icon { width: 12px; height: 12px; flex: none; margin-top: 2px; }

  /* Front card */
  .card--front {
    display: flex;
    align-items: center;
    justify-content: center;
  }
  .card--front .brand { text-align: center; }
  .card--front .brand__name { font-size: 80px; }
  .card--front .brand__tagline { font-size: 17px; margin-top: 10px; letter-spacing: 0.5px; }
</style>
</head>
<body>
<main class="canvas">

  <section class="card card--back" aria-label="Business card back">
    <div class="card__info">
      <div class="brand">
        <p class="brand__name">Lumora</p>
        <p class="brand__tagline">networks · cloud · support</p>
      </div>

      <ul class="contacts">
        <li class="contacts__item">
          <svg class="contacts__icon" viewBox="0 0 12 12"><path d="M6 0.5a4 4 0 0 0-4 4c0 3 4 7 4 7s4-4 4-7a4 4 0 0 0-4-4z" fill="var(--orange)"/><circle cx="6" cy="4.5" r="1.4" fill="#fff"/></svg>
          <span>123, Main Street, Anytown,<br>Postal Code, Country</span>
        </li>
        <li class="contacts__item">
          <svg class="contacts__icon" viewBox="0 0 12 12"><path d="M2.5 1h2l1 3-1.3 1a6 6 0 0 0 2.8 2.8l1-1.3 3 1v2A1.5 1.5 0 0 1 9.5 11 8.5 8.5 0 0 1 1 2.5 1.5 1.5 0 0 1 2.5 1z" fill="var(--orange)"/></svg>
          <span>555-1234-56<br>555-1234-56</span>
        </li>
        <li class="contacts__item">
          <svg class="contacts__icon" viewBox="0 0 12 12"><rect x="0.5" y="2" width="11" height="8" rx="1" fill="var(--orange)"/><path d="M1 2.5l5 4 5-4" stroke="#fff" stroke-width="1" fill="none"/></svg>
          <span>we@youraddress.com</span>
        </li>
        <li class="contacts__item">
          <svg class="contacts__icon" viewBox="0 0 12 12"><circle cx="6" cy="6" r="5.5" fill="var(--orange)"/><path d="M0.8 6h10.4M6 0.5c-2.5 3-2.5 8 0 11M6 0.5c2.5 3 2.5 8 0 11" stroke="#fff" stroke-width="0.8" fill="none"/></svg>
          <span>www.yourwebsite.com</span>
        </li>
      </ul>
    </div>
    <div class="card__panel">
      <h1 class="person__name">Daniel Reyes</h1>
      <p class="person__role">Chief Executive Officer</p>
    </div>
  </section>

  <section class="card card--front" aria-label="Business card front">
    <div class="brand">
      <p class="brand__name">Lumora</p>
      <p class="brand__tagline">networks · cloud · support</p>
    </div>
  </section>

</main>
</body>
</html>
```